Business card design for engineering firm specializing in defense industry.

We need a professional business card design. Something simple but stands out. We are an engineering company specializing in composites in the defense industry.
Industry/Entity Type
Defense
Contact Information for Business Card
A simple black business card with the Varlonix yellow color is what we had in mind but open for other designs.
Colors
ffc214

```html
<!DOCTYPE html>
<html lang="en">
<head>
<meta charset="utf-8">
<title>Varlonix Business Card</title>
<link rel="stylesheet" href="https://fonts.googleapis.com/css2?family=Roboto:wght@400;500;700;900&display=swap">
<style>
  :root {
    --backdrop: #2a2a2a;
    --card-dark: #231f20;
    --card-light: #ffffff;
    --brand-yellow: #ffc214;
    --text-light: #ffffff;
    --text-dark: #231f20;
  }
  html, body {
    margin: 0;
    padding: 0;
    width: 1200px;
    height: 900px;
    overflow: hidden;
    background: var(--backdrop);
    font-family: "Roboto", Arial, sans-serif;
  }
  .canvas {
    position: relative;
    width: 1200px;
    height: 900px;
  }
  .card {
    position: absolute;
    top: 300px;
    width: 516px;
    height: 297px;
    box-shadow: 0 6px 18px rgba(0,0,0,0.45);
    overflow: hidden;
  }
  .card-front {
    left: 73px;
    background: var(--card-dark);
  }
  .card-back {
    left: 616px;
    background: var(--card-light);
  }
  .wordmark {
    position: absolute;
    left: 0;
    right: 0;
    display: flex;
    align-items: center;
    justify-content: center;
    gap: 12px;
    font-weight: 900;
    letter-spacing: 0.5px;
    line-height: 1;
  }
  .wordmark-square {
    width: 30px;
    height: 30px;
    background: var(--brand-yellow);
  }
  .card-front .wordmark {
    top: 122px;
    font-size: 46px;
    color: var(--text-light);
  }
  .card-back .wordmark {
    top: 42px;
    font-size: 42px;
    color: var(--text-dark);
  }
  .card-back .wordmark-square {
    width: 27px;
    height: 27px;
  }
  .website {
    position: absolute;
    top: 257px;
    left: 0;
    right: 0;
    text-align: center;
    font-size: 13px;
    font-weight: 700;
    color: var(--brand-yellow);
  }
  .info-band {
    position: absolute;
    left: 0;
    right: 0;
    top: 156px;
    bottom: 0;
    background: var(--card-dark);
  }
  .info-band::before {
    content: "";
    position: absolute;
    left: 0;
    right: 0;
    top: 0;
    height: 4px;
    background: var(--brand-yellow);
  }
  .contact-block {
    position: absolute;
    left: 0;
    right: 0;
    top: 185px;
    text-align: center;
    color: var(--text-light);
  }
  .person-name {
    margin: 0;
    font-size: 17px;
    font-weight: 700;
    letter-spacing: 1.5px;
    color: var(--brand-yellow);
  }
  .person-role {
    margin: 3px 0 0;
    font-size: 12.5px;
    letter-spacing: 1px;
  }
  .contact-line {
    margin: 14px 0 0;
    font-size: 12.5px;
    display: flex;
    justify-content: center;
    align-items: center;
    gap: 8px;
  }
  .contact-item {
    display: inline-flex;
    align-items: center;
    gap: 4px;
  }
  .contact-icon {
    width: 11px;
    height: 11px;
    fill: var(--brand-yellow);
  }
  .address {
    margin: 4px 0 0;
    font-size: 12.5px;
  }
</style>
</head>
<body>
<main class="canvas">

  <section class="card card-front" aria-label="Business card front">
    <div class="wordmark"><span class="wordmark-square"></span>Varlonix</div>
    <div class="website">www.varlonix.com</div>
  </section>

  <section class="card card-back" aria-label="Business card back">
    <div class="info-band"></div>
    <div class="wordmark"><span class="wordmark-square"></span>Varlonix</div>
    <div class="contact-block">
      <p class="person-name">DANIEL HARWICK</p>
      <p class="person-role">MANAGING DIRECTOR</p>
      <p class="contact-line">
        <span class="contact-item">
          <svg class="contact-icon" viewBox="0 0 24 24" aria-hidden="true"><path d="M6.6 10.8a15.1 15.1 0 0 0 6.6 6.6l2.2-2.2a1 1 0 0 1 1-.25 11.4 11.4 0 0 0 3.6.57 1 1 0 0 1 1 1V20a1 1 0 0 1-1 1A17 17 0 0 1 3 4a1 1 0 0 1 1-1h3.5a1 1 0 0 1 1 1c0 1.25.2 2.45.57 3.57a1 1 0 0 1-.25 1z"/></svg>
          555 010 20 30
        </span>
        <span class="contact-item">
          <svg class="contact-icon" viewBox="0 0 24 24" aria-hidden="true"><path d="M2 6l10 7 10-7v12H2z"/><path d="M2 5h20l-10 7z"/></svg>
          d.harwick@varlonix.com
        </span>
      </p>
      <p class="address">48 Sample Avenue, Lakeview, New York 10025</p>
    </div>
  </section>

</main>
</body>
</html>
```